Ravelor Global Kft. is an online recruitment marketplace connecting the employers and recruiters together. We provide an e-bussiness solution for companies and give busines opportunity for recruiters.
We have a logo design already, which should be used on the business card.
Our colours are grey and magenta, which can be seen in the logo. Black is also welcome.
The style should be dynamic, young but professional. It should be clear, visible, elegant, not too crowded, simple but exciting.
We need the following data on the BC: name, title, address, phone,fax and mobile number, email address, website.
Target Market(s)
Our target market are companies, as this is a B2B business. We also target recruiters, recruitment professionals, headhunters.We would like to be impressive and different.
Industry/Entity Type
Business
Requirements
Must have
- We would like to promote our website, www.ravelorglb.hu.
- Please, put this on the back with a quite visible letter size.The style should be dynamic, young but professional. It should be clear, visible, elegant, not too crowded, simple but exciting.
Should not have
- We do not want to see people figures.

```html
<!DOCTYPE html>
<html lang="en">
<head>
<meta charset="utf-8">
<title>Ravelor Global Kft. – Business Card</title>
<link rel="stylesheet" href="https://fonts.googleapis.com/css2?family=Ubuntu:wght@400;500;700&display=swap">
<style>
  :root {
    --magenta: #b51f76;
    --magenta-dark: #9c1864;
    --ink: #111111;
    --paper: #ffffff;
    --paper-shade: #e4e4e4;
    --page: #ffffff;
  }
  html, body {
    margin: 0;
    padding: 0;
    width: 1200px;
    height: 900px;
    overflow: hidden;
    background: var(--page);
    font-family: "Ubuntu", Arial, sans-serif;
  }
  .canvas {
    position: relative;
    width: 1200px;
    height: 900px;
  }
  .card {
    position: absolute;
    left: 48px;
    top: 128px;
    width: 1108px;
    height: 628px;
    overflow: hidden;
    box-shadow: 0 4px 14px rgba(0,0,0,0.25);
  }
  .card-texture {
    position: absolute;
    inset: 0;
    background: radial-gradient(ellipse at 55% 45%, var(--paper) 0%, #f6f6f6 45%, var(--paper-shade) 100%);
  }
  .brand-mark {
    position: absolute;
    left: 42px;
    top: 52px;
    width: 180px;
    height: 180px;
    background: var(--magenta);
  }
  .brand-name {
    position: absolute;
    left: 240px;
    top: 150px;
    margin: 0;
    font-size: 46px;
    font-weight: 700;
    line-height: 1;
    color: var(--magenta);
    white-space: nowrap;
  }
  .website {
    position: absolute;
    left: 176px;
    top: 262px;
    margin: 0;
    font-size: 30px;
    line-height: 1;
    color: var(--ink);
  }
  .contact-line {
    position: absolute;
    right: 52px;
    margin: 0;
    line-height: 1;
    color: var(--ink);
    text-align: right;
    white-space: nowrap;
  }
  .person-name { top: 292px; font-size: 50px; }
  .person-title { top: 368px; font-size: 25px; }
  .mobile { top: 428px; font-size: 44px; }
  .email { top: 474px; font-size: 31px; }
  .footer-band {
    position: absolute;
    left: 0;
    right: 0;
    bottom: 0;
    height: 80px;
    background: linear-gradient(to bottom, var(--magenta), var(--magenta-dark));
    display: flex;
    align-items: center;
    justify-content: center;
    color: var(--paper);
    font-size: 28px;
    white-space: pre;
  }
</style>
</head>
<body>
<div class="canvas">
  <div class="card">
    <div class="card-texture" role="img" aria-label="Faint light grey jigsaw puzzle background pattern"></div>

    <div class="brand-mark"></div>
    <p class="brand-name">Ravelor Global Kft.</p>
    <p class="website">www.ravelorglb.hu</p>

    <p class="contact-line person-name">Dóra Halmi</p>
    <p class="contact-line person-title">managing director</p>
    <p class="contact-line mobile">+36 (30) 555-0182</p>
    <p class="contact-line email">halmid@ravelorglb.hu</p>

    <div class="footer-band">1061 Budapest, Fenyves utca 8.  +36 (1) 555-0147</div>
  </div>
</div>
</body>
</html>
```